Marigold Premium Business Card Design Project

About the company: Here at Fernhaven Botanics, we focus on cosmetic products that based on essential oils and different kinds of plant essences. All of our raw materials are pure organic and specially selected from local producers in Australia.

I'm here to look for a unique business card design, to replace the current one later on, so I don't have many requirements. Why I wanna restrict designers' creativity?

All I know is: 1. do not make it too complicated, straight forward, simple and pure. 2. this design may be used for other purposes (i.e. logo and slogan on the front, Brand Story and contact details at the back). Therefor, I'd like to have the design for 3 layouts, one only have logo, slogan, contact detials, one for the brand story, the other one for the personal business card with staff's mob etc...

A vector graphic is required, i.e. eps, ai, easy for me to resize.

Round Corner.

Thanks

Plz add "Hand made in Australia" in the design, cheers.

Target Market(s)

Women aged yr 20-50

Industry/Entity Type

Business

Requirements
Must have
• Logo: please see attacment (eps, ai)

Slogan: Moonlit Velvet Glow

Website:www.fernhavenbotanics.com.au

Address: temporary not available

Phone: temporary not available

"Hand made in Australia"

Nice to have
• Prefer round corner

```html
<!DOCTYPE html>
<html lang="en">
<head>
<meta charset="utf-8">
<title>Fernhaven Botanics – Business Cards</title>
<link href="https://fonts.googleapis.com/css2?family=Oswald:wght@300;400&display=swap" rel="stylesheet">
<style>
  :root {
    --backdrop: #f5dce8;
    --card: #ffffff;
    --brand-pink: #e2456f;
    --text-pink: #f08c9c;
    --ornament-grey: #a9a9a9;
    --name-grey: #5a5a5a;
    --card-shadow: rgba(160, 90, 120, 0.25);
  }
  * { box-sizing: border-box; margin: 0; padding: 0; }
  html, body {
    width: 1200px;
    height: 2526px;
    overflow: hidden;
  }
  body {
    background: var(--backdrop);
    font-family: "Oswald", sans-serif;
    font-weight: 300;
    position: relative;
  }
  .card {
    position: absolute;
    left: 164px;
    width: 872px;
    height: 531px;
    background: var(--card);
    border-radius: 38px;
    box-shadow: 0 4px 10px var(--card-shadow);
  }
  .card--front { top: 290px; }
  .card--story { top: 972px; }
  .card--staff { top: 1657px; }

  .brand-name {
    position: absolute;
    top: 118px;
    left: 0;
    width: 100%;
    text-align: center;
    font-size: 62px;
    font-weight: 400;
    letter-spacing: 6px;
    text-transform: uppercase;
    color: var(--brand-pink);
    line-height: 1;
  }
  .slogan {
    position: absolute;
    left: 0;
    width: 100%;
    display: flex;
    justify-content: center;
    align-items: center;
    gap: 14px;
    font-size: 20px;
    letter-spacing: 1.5px;
    text-transform: uppercase;
    color: var(--text-pink);
    line-height: 1;
  }
  .slogan::before, .slogan::after {
    content: "";
    width: 52px;
    height: 2px;
    background: var(--ornament-grey);
  }
  .plus {
    position: absolute;
    left: 0;
    width: 100%;
    text-align: center;
    font-size: 14px;
    color: var(--ornament-grey);
    line-height: 1;
  }
  .brace {
    position: absolute;
    left: 396px;
    width: 80px;
    height: 16px;
  }
  .brace path { fill: none; stroke: var(--ornament-grey); stroke-width: 3; }

  .made-in {
    position: absolute;
    right: 472px;
    font-size: 15px;
    letter-spacing: 1.5px;
    text-transform: uppercase;
    color: var(--text-pink);
    line-height: 1;
  }
  .divider {
    position: absolute;
    left: 435px;
    width: 1px;
    background: var(--ornament-grey);
  }
  .contact {
    position: absolute;
    left: 463px;
    list-style: none;
    font-size: 15px;
    letter-spacing: 1.5px;
    text-transform: uppercase;
    color: var(--text-pink);
    line-height: 24px;
  }
  .contact .staff-name { color: var(--name-grey); font-weight: 400; }

  .story {
    position: absolute;
    top: 352px;
    left: 150px;
    width: 572px;
    font-size: 16.5px;
    line-height: 24.5px;
    text-align: justify;
    color: var(--text-pink);
  }
  .side-brace {
    position: absolute;
    top: 346px;
    width: 18px;
    height: 100px;
  }
  .side-brace path { fill: none; stroke: var(--ornament-grey); stroke-width: 3; }
</style>
</head>
<body>

  <!-- Layout 1: logo, slogan, contact details -->
  <section class="card card--front">
    <div class="brand-name">Fernhaven Botanics</div>
    <svg class="brace" style="top:280px" viewBox="0 0 80 16"><path d="M2 14 Q2 4 12 4 L32 4 Q40 4 40 0 Q40 4 48 4 L68 4 Q78 4 78 14"/></svg>
    <div class="slogan" style="top:325px">Moonlit Velvet Glow</div>
    <div class="plus" style="top:370px">+</div>
    <div class="made-in" style="top:402px">Hand made in Australia</div>
    <div class="divider" style="top:394px;height:73px"></div>
    <ul class="contact" style="top:398px">
      <li>P: Your phone number.</li>
      <li>A: Your address.</li>
      <li>W: www.fernhavenbotanics.com.au</li>
    </ul>
    <svg class="brace" style="top:490px" viewBox="0 0 80 16"><path d="M2 2 Q2 12 12 12 L32 12 Q40 12 40 16 Q40 12 48 12 L68 12 Q78 12 78 2"/></svg>
  </section>

  <!-- Layout 2: brand story -->
  <section class="card card--story">
    <div class="brand-name">Fernhaven Botanics</div>
    <div class="slogan" style="top:283px">Moonlit Velvet Glow</div>
    <div class="plus" style="top:318px">+</div>
    <svg class="side-brace" style="left:114px" viewBox="0 0 18 100"><path d="M16 2 Q6 2 6 12 L6 40 Q6 50 0 50 Q6 50 6 60 L6 88 Q6 98 16 98"/></svg>
    <p class="story">Your Brand Story. Lorem Ipsum is simply dummy text of the printing and typesetting industry. Lorem Ipsum has been the industry's standard dummy text ever since the 1500s, when an unknown printer took a galley of type and scrambled it to make a type specimen book.</p>
    <svg class="side-brace" style="left:740px" viewBox="0 0 18 100"><path d="M2 2 Q12 2 12 12 L12 40 Q12 50 18 50 Q12 50 12 60 L12 88 Q12 98 2 98"/></svg>
  </section>

  <!-- Layout 3: personal staff card -->
  <section class="card card--staff">
    <div class="brand-name">Fernhaven Botanics</div>
    <svg class="brace" style="top:266px" viewBox="0 0 80 16"><path d="M2 14 Q2 4 12 4 L32 4 Q40 4 40 0 Q40 4 48 4 L68 4 Q78 4 78 14"/></svg>
    <div class="slogan" style="top:312px">Moonlit Velvet Glow</div>
    <div class="plus" style="top:352px">+</div>
    <div class="made-in" style="top:388px">Hand made in Australia</div>
    <div class="divider" style="top:384px;height:98px"></div>
    <ul class="contact" style="top:384px">
      <li class="staff-name">Staff's name</li>
      <li>P: Your phone number.</li>
      <li>A: Your address.</li>
      <li>W: www.fernhavenbotanics.com.au</li>
    </ul>
    <svg class="brace" style="top:492px" viewBox="0 0 80 16"><path d="M2 2 Q2 12 12 12 L32 12 Q40 12 40 16 Q40 12 48 12 L68 12 Q78 12 78 2"/></svg>
  </section>

</body>
</html>
```